Modern Small Law Firm Website To Look Cutting Edge

I need a website design for a new, single-attorney law firm. The firm will be called "The Thornwell Law Group." Our goal is to handle car accident and general personal injury lawsuits for individuals.

Our selling points are: (1) We charge less so you keep more; (2) We have experience and success trying and settling multi-million dollar cases; (3) We use modern technology to make the whole process simple, easy and hassle-free for clients.

Also because we are a one-man law firm, the clients will personally know the lawyer and have access to them. For that reason, I thought a good big tagline for the website would be "KNOW YOUR LAWYER"

I like the idea of splitting the website vertically down the middle, with the left side having a blue background, a picture of me, and big white lettering for the tagline, and the right side having a white background with blue lettering and headlines. I don't want navy blue or royal blue, but a more bright and eye-catching blue color. We can experiment with different shades.

I would be curious about how it could look with some minor orange accent coloring somewhere.

I need to feature prominently, probably in the top left corner, this phone number: 504-917-2083.

This will be used as much by mobile users as it would be by desktop/computer users.

The final design should communicate trust, convenience and cutting edge technology that leads to success.

Finally, I would be curious how we can have a sleek looking info submission box somewhere on the right side nearer the bottom that features different combinations of presenting these phrases: "QUICK QUESTION? QUICK ANSWER" The info submission button could say "Ask"

I am uploading two different pictures of me that can be used. The gray backgrounds are not necessary or good, if there is a way to cut them out that would be great. I can try and get that if needed.

Target Market(s)

Individuals who have been hurt by others, mostly in car accidents. They will be frustrated, inconvenienced and need to be soothed.

Industry/Entity Type

Legal

Number of Pages Required

1 page

Font styles to use
Sans Serif

Colors
0692cd
33a6d7
85cae6
faa54b
f78f20
3276b5

Requirements
Must have
• If you have started designing already, please note that the project description information is more important than the image that I uploaded originally. It has since been deleted.
• Also please now use the color photo that has been uploaded.
Nice to have
• I really want a clean and simple website design with not a lot of clutter. I'd like to avoid the typical law firm websites that you see that have tool bars across the top and basic borders/columns everywhere. It needs to grab your attention and look a little more cutting edge and different.
• Let's experiment with different eye-catching ways to present the three value propositions I noted.
• Also if the screen is split vertically with the left and right side being blue and white, maybe we can experiment with different ways that the two colors could fade into each other as opposed to just a line where one color starts and the other ends.
• And maybe the blue/white backgrounds could be textured somehow so that they don't appear flat. Perhaps we could try using differing shades of blue to give the appearance of pattern or 3D texture.
Should not have
• The basic picture/design I uploaded is just a suggestion, but there isn't really anything there.

```html
<!DOCTYPE html>
<html lang="en">
<head>
<meta charset="utf-8">
<title>The Thornwell Law Group</title>
<link href="https://fonts.googleapis.com/css2?family=Oswald:wght@400;500&family=Open+Sans:wght@400;600;700&display=swap" rel="stylesheet">
<style>
  :root {
    --blue: #0692cd;
    --blue-mid: #1d8ccb;
    --blue-deep: #1a5f8e;
    --ink: #333;
    --muted: #6c6c6c;
    --white: #fff;
    --dark: #1d1d1d;
    --footer: #2b3a46;
  }
  * { margin: 0; padding: 0; box-sizing: border-box; }
  html, body { width: 714px; height: 1200px; overflow: hidden; background: var(--white); }
  body { position: relative; font-family: "Open Sans", Arial, sans-serif; color: var(--ink); }

  .hero { position: absolute; left: 0; top: 0; width: 714px; height: 392px; }
  .hero-photo { position: absolute; inset: 0; background: linear-gradient(100deg, #4d5a64 0%, #8e9aa3 35%, #c6ced3 60%, #7f8d97 100%); }
  .topbar { position: absolute; left: 0; top: 0; width: 714px; height: 48px; background: rgba(22, 78, 120, .88); display: flex; align-items: center; justify-content: space-between; padding: 0 18px; }
  .brand { color: var(--white); font-family: "Oswald", sans-serif; font-weight: 400; font-size: 17px; letter-spacing: .3px; }
  .contact { display: flex; align-items: center; gap: 10px; }
  .contact-ask { color: var(--white); font-family: "Oswald", sans-serif; font-size: 14px; letter-spacing: .6px; }
  .contact-phone { display: flex; align-items: center; gap: 8px; background: rgba(255,255,255,.15); padding: 6px 10px; color: var(--white); font-size: 11px; }
  .contact-phone strong { font-size: 15px; font-weight: 700; letter-spacing: .5px; }
  .tagline { position: absolute; left: 415px; top: 160px; color: var(--white); font-family: "Oswald", sans-serif; font-weight: 500; text-transform: uppercase; line-height: 1; text-shadow: 0 2px 6px rgba(0,0,0,.35); }
  .tagline span { display: block; }
  .tagline .l1 { font-size: 48px; letter-spacing: 1px; }
  .tagline .l2 { font-size: 60px; margin-top: 4px; }
  .scroll-cue { position: absolute; left: 337px; top: 370px; width: 42px; height: 42px; border-radius: 50%; background: #3d4a55; display: flex; align-items: center; justify-content: center; z-index: 2; }

  .row { position: absolute; left: 0; width: 714px; }
  .half { position: absolute; top: 0; height: 100%; width: 357px; }
  .left { left: 0; }
  .right { left: 357px; }
  .copy { padding: 0 34px 0 40px; display: flex; flex-direction: column; justify-content: center; }
  .copy h2 { font-family: "Oswald", sans-serif; font-weight: 500; font-size: 30px; color: var(--blue); text-transform: uppercase; line-height: 1.1; text-align: right; }
  .copy .lead { font-size: 12.5px; font-weight: 700; color: var(--ink); margin-top: 8px; text-align: right; }
  .copy p.body { font-size: 10.5px; line-height: 1.55; color: var(--muted); margin-top: 8px; text-align: right; }
  .btn { align-self: flex-end; margin-top: 14px; background: var(--blue); color: var(--white); font-size: 9.5px; font-weight: 700; text-transform: uppercase; padding: 7px 12px; letter-spacing: .5px; }
  .panel-blue { background: var(--blue-mid); }
  .panel-blue h2, .panel-blue .lead, .panel-blue p.body { color: var(--white); text-align: left; }
  .panel-blue p.body { color: #e3f2fb; }
  .panel-blue .btn { align-self: flex-start; background: var(--dark); }
  .photo-fill { width: 100%; height: 100%; }

  .footer { position: absolute; left: 0; top: 1176px; width: 714px; height: 24px; background: var(--footer); color: #c9d3da; font-size: 9px; display: flex; align-items: center; justify-content: center; }
</style>
</head>
<body>
  <header class="hero">
    <div class="hero-photo" role="img" aria-label="Attorney in a suit standing in front of parked cars, muted blue-grey tones"></div>
    <div class="topbar">
      <div class="brand">The Thornwell Law Group</div>
      <div class="contact">
        <span class="contact-ask">HAVING A QUESTION ?</span>
        <span class="contact-phone">Call Us : <strong>504-917-2083</strong></span>
      </div>
    </div>
    <h1 class="tagline"><span class="l1">Know Your</span><span class="l2">Lawyer</span></h1>
  </header>
  <div class="scroll-cue">
    <svg width="18" height="12" viewBox="0 0 18 12"><path d="M2 2 L9 9 L16 2" fill="none" stroke="#fff" stroke-width="2.5"/></svg>
  </div>

  <section class="row" style="top:412px;height:233px;">
    <div class="half left copy">
      <h2>Never more than 24%</h2>
      <div class="lead">Our lawyers will never overcharge you like others will.</div>
      <p class="body">We keep our fees low so more of your settlement stays with you. Every charge is explained up front, in plain words, with no surprise costs at the end of your case and no hidden extras.</p>
      <span class="btn">Read more &gt;</span>
    </div>
    <div class="half right" role="img" aria-label="Hand with a pencil working on a calculator and paperwork" style="background:linear-gradient(135deg,#f4efe6 0%,#e0d6c6 45%,#8a8f95 100%);"></div>
  </section>

  <section class="row" style="top:645px;height:260px;">
    <div class="half left" role="img" aria-label="Client shaking hands with an agent beside a car" style="background:linear-gradient(120deg,#c9d3dc 0%,#7e8c98 50%,#3d4650 100%);"></div>
    <div class="half right copy panel-blue">
      <h2>We make it easy</h2>
      <div class="lead">Modern tools make your claim simple, fast and hassle-free.</div>
      <p class="body">Track your claim online, sign papers from your phone and reach your lawyer directly. We handle the forms, the calls and the insurers so you can focus on getting well again.</p>
      <span class="btn">Read more &gt;</span>
    </div>
  </section>

  <section class="row" style="top:905px;height:271px;">
    <div class="half left copy">
      <h2>Big firm lawyering</h2>
      <div class="lead">With experience in multi-million dollar litigation, we're the best.</div>
      <p class="body">Your case gets the same care and preparation as a major firm would give it. We have tried and settled large claims and bring that experience to every client we serve.</p>
      <span class="btn">Read more &gt;</span>
    </div>
    <div class="half right" role="img" aria-label="Lawyer meeting clients at a desk in front of a bookshelf" style="background:linear-gradient(160deg,#6b4a32 0%,#a07a55 40%,#e4ddd4 75%,#3a3f47 100%);"></div>
  </section>

  <footer class="footer">Copyright © 2016 The Thornwell Law Group. All Rights Reserved.</footer>
</body>
</html>
```